Pig club info pack flyers

We need base artwork to which we can add headings and content. we are looking for double sided A4 designs with blank Word suitable blocks which can hold content on topics including the law, research findings, zoonotic diseases etc etc.
We want them bright but not too complex nor too cartoonish. they object is to be eye-catching but credible. Colours should reflect our logo colours. The running pig line art, if used, should be the yellow in our logo. Maybe a standard heading such as THE FACTS. Open to all ideas.
Target Market(s)
Potential members, existing members, land managers
Industry/Entity Type
Conservation/hunting

```html
<!DOCTYPE html>
<html lang="en">
<head>
<meta charset="utf-8">
<title>Info Pack Flyer</title>
<link href="https://fonts.googleapis.com/css2?family=Quicksand:wght@400;500;700&display=swap" rel="stylesheet">
<style>
  :root {
    --page-bg: #ecebe8;
    --red-bright: #c62127;
    --red-deep: #7c1d22;
    --red-shadow: #4f1014;
    --white: #ffffff;
    --club-blue: #1f4fa3;
  }
  * { margin: 0; padding: 0; box-sizing: border-box; }
  html, body {
    width: 1200px; height: 1200px; overflow: hidden;
    background: var(--page-bg);
    font-family: "Quicksand", sans-serif;
  }
  .flyer {
    position: absolute; left: 200px; top: 84px;
    width: 800px; height: 1032px;
    overflow: hidden;
    box-shadow: 0 4px 14px rgba(0,0,0,0.18);
  }
  .flyer__shapes { position: absolute; inset: 0; width: 100%; height: 100%; }
  .club-badge {
    position: absolute; left: 475px; top: 50px;
    width: 275px; height: 185px;
    background: var(--white);
    display: flex; align-items: center; justify-content: center; gap: 12px;
    padding: 18px;
  }
  .club-badge__dot {
    width: 22px; height: 22px; border-radius: 50%;
    background: var(--club-blue); flex: none;
  }
  .club-badge__name {
    color: var(--club-blue);
    font-weight: 700; font-size: 21px; line-height: 1.2;
    text-transform: uppercase;
  }
  .headline {
    position: absolute; left: 52px; top: 366px;
    color: var(--white);
    font-weight: 700; font-size: 64px; line-height: 59px;
    letter-spacing: 0.5px;
  }
  .body-copy {
    position: absolute; left: 52px; top: 598px;
    width: 328px;
    color: var(--white);
    font-weight: 400; font-size: 14.6px; line-height: 20.7px;
    letter-spacing: 0.2px;
    text-align: justify;
    hyphens: auto;
  }
</style>
</head>
<body>
  <main class="flyer">
    <svg class="flyer__shapes" viewBox="0 0 640 826" preserveAspectRatio="none">
      <defs>
        <linearGradient id="boarTone" x1="0" y1="0" x2="0" y2="1">
          <stop offset="0" stop-color="#7c1d22" stop-opacity="0"/>
          <stop offset="0.35" stop-color="#6a171c" stop-opacity="0.55"/>
          <stop offset="1" stop-color="#4f1014" stop-opacity="0.85"/>
        </linearGradient>
        <radialGradient id="boarBody" cx="0.72" cy="0.45" r="0.42">
          <stop offset="0" stop-color="#3d0b0e" stop-opacity="0.75"/>
          <stop offset="1" stop-color="#3d0b0e" stop-opacity="0"/>
        </radialGradient>
      </defs>
      <rect class="base" width="640" height="826" fill="var(--red-deep)"/>
      <path class="corner-top" d="M0 0 H298 Q298 126 200 128 H0 Z" fill="var(--red-bright)"/>
      <rect class="margin-left" x="0" y="128" width="27" height="698" fill="var(--red-bright)"/>
      <path class="block-right" d="M330 826 V330 Q334 256 402 253 H640 V826 Z" fill="var(--red-bright)"/>
      <g role="img" aria-label="Photograph of a wild boar standing in a forest clearing, red duotone">
        <rect x="0" y="330" width="640" height="496" fill="url(#boarTone)"/>
        <rect x="230" y="330" width="410" height="496" fill="url(#boarBody)"/>
      </g>
      <polygon class="rule-top" points="27,122 205,126 205,131 27,129" fill="var(--white)"/>
      <polygon class="rule-bottom" points="150,763 330,767 330,773 150,769" fill="var(--white)"/>
      <rect role="img" aria-label="Running pig line art in white" x="72" y="181" width="218" height="112" fill="var(--white)" fill-opacity="0.06"/>
    </svg>

    <div class="club-badge">
      <span class="club-badge__dot"></span>
      <span class="club-badge__name">Southern Ridge Hunters Guild</span>
    </div>

    <h1 class="headline">LOREM<br>IPSUM<br>IS SIMPLY</h1>

    <p class="body-copy">Lorem Ipsum is simply dummy text of the printing and typesetting industry. Lorem Ipsum has been the industry's standard dummy text ever since the 1500s, when an unknown printer took a galley of type and scrambled it to make a type specimen book. It has survived not only five centuries, but also the leap into electronic typesetting, remaining essentially unchanged. It was popularised in the 1960s with the release of Letraset sheets containing Lorem Ipsum passages, and more recently with desktop publishing software like Aldus PageMaker including versions of Lorem Ipsum.</p>
  </main>
</body>
</html>
```